GravaLoop. Customer needs to know about us, what services we provide & contact us

We are a waste tire recycling company. Our primary focus is on providing a sustainable and cost effective service focusing on: Waste Tire Management, Hassle Free Scheduling for Tire Collection, Mobile Shredding & Special site cleanup services. GravaLoop will be producing TDF, Clean Tire Wire & further materials.
Please look at https://harvonrubber.example
Please look at https://quelbamaterials.example

This is the look and feel of what we want

I have attached a word document with our website info.

Target Market(s)

Tire Install Companies. Such as morbanhaul.example. TDF Purchasers such as pelkofuel.example.

Industry/Entity Type

Waste Tire Recycling

Coding

Coded - Design and coding required

Number of Pages Required

3 page

Font styles to use
Other font styles liked:
• Look at our logo

Requirements
Must have
• We need a 3 page setup for About Us, Services & Contact Us. Contact us should be a form them can fill out and submit to us Images that are related to waste tire recycling. Clean, modern, innovative.
Nice to have
• The color and feel of the website should work with our logo that we did with artpivot
Should not have
• Anything progressive, political or "woke"

```html
<!DOCTYPE html>
<html lang="en">
<head>
<meta charset="utf-8">
<title>GravaLoop – Waste Tire Recycling</title>
<link rel="stylesheet" href="https://fonts.googleapis.com/css2?family=Poppins:wght@400;500;600;700&family=Roboto+Condensed:wght@700&display=swap">
<style>
:root{
  --green:#0f9440;
  --green-soft:#3fae63;
  --ink:#1b1b1b;
  --body:#2c2c2c;
  --white:#ffffff;
  --grey-band:#f1f1f1;
  --charcoal:#2f2f2f;
}
*{box-sizing:border-box;margin:0;padding:0}
html,body{width:1200px;height:4164px;overflow:hidden}
body{position:relative;background:var(--white);font-family:"Poppins",sans-serif;color:var(--body)}
.abs{position:absolute}
.heading{font-family:"Roboto Condensed",sans-serif;font-weight:700;font-size:34px;color:var(--ink);display:flex;align-items:center;gap:8px;white-space:nowrap}
.heading .accent{color:var(--green)}
.heading .dot{width:30px;height:30px;border-radius:50%;background:var(--green);display:inline-block}
.btn{position:absolute;background:var(--green);color:var(--white);font-size:14px;display:flex;align-items:center;justify-content:center;text-decoration:none;letter-spacing:.3px}
p.copy{font-size:13.5px;line-height:24.5px;letter-spacing:.4px}
.photo{position:absolute}

/* hero */
.hero-photo{position:absolute;left:0;top:0;width:1200px;height:580px;
  background:linear-gradient(180deg,#6b6e72 0%,#4a4c4f 35%,#3a4452 60%,#7b6a58 100%);
  clip-path:polygon(0 0,1200px 0,1200px 356px,0 542px)}
.hero-band{position:absolute;left:0;top:0;width:1200px;height:600px}
.logo{position:absolute;display:flex;align-items:center;gap:10px;font-family:"Poppins",sans-serif;font-weight:700;font-size:40px;letter-spacing:-.5px}
.logo .mark{width:30px;height:30px;border-radius:50%}
.topbar{position:absolute;top:24px;left:702px;display:flex;gap:28px;color:var(--white);font-size:14px;align-items:center}
.topbar span{display:flex;align-items:center;gap:9px}
.nav{position:absolute;top:60px;left:684px;display:flex;color:var(--white);font-size:14px}
.nav a{color:inherit;text-decoration:none}
.hero-title{position:absolute;top:182px;left:0;width:1200px;text-align:center;color:var(--white);font-weight:700;font-size:26px;line-height:35px}

/* about */
.about-panel{position:absolute;left:162px;top:830px;width:876px;height:1065px;background:var(--green)}
.about-copy p.copy{color:var(--white)}
.about-copy b{font-weight:700}

/* services */
.service-card{position:absolute;top:2029px;width:205px;text-align:center}
.service-card .photo{position:relative;width:205px;height:199px}
.service-card h3{font-weight:400;font-size:15px;line-height:20px;margin-top:24px;color:var(--ink)}
.service-card.active h3{color:var(--green);font-weight:600}

/* footer */
.contact-box{position:absolute;top:3994px;width:267px;height:97px;border:1.5px solid var(--green);display:flex;align-items:center;padding-left:24px;gap:16px;font-size:13px;line-height:20px;color:var(--ink);white-space:nowrap}
.contact-box b{font-weight:600}
.footer-nav{position:absolute;top:3946px;font-size:14px;color:var(--ink)}
</style>
</head>
<body>

<!-- HERO -->
<div class="hero-photo" role="img" aria-label="Pile of scrap tires stacked on a blue shipping container outdoors"></div>
<svg class="hero-band" viewBox="0 0 1200 600" aria-hidden="true">
  <polygon points="0,530 1200,345 1200,395 0,585" fill="var(--green-soft)"/>
  <polygon points="0,585 1200,395 1200,600 0,600" fill="#ffffff"/>
</svg>

<div class="logo" style="left:162px;top:30px;color:var(--white)"><span class="mark" style="background:var(--white)"></span>GravaLoop</div>
<div class="topbar">
  <span><svg width="22" height="15" viewBox="0 0 22 15"><rect x="1" y="1" width="20" height="13" fill="none" stroke="#fff" stroke-width="1.6"/><path d="M1 1l10 8 10-8" fill="none" stroke="#fff" stroke-width="1.6"/></svg>info@gravaloop.example</span>
  <span><svg width="17" height="17" viewBox="0 0 24 24"><path d="M6.6 10.8a15.1 15.1 0 0 0 6.6 6.6l2.2-2.2a1 1 0 0 1 1-.25 11.4 11.4 0 0 0 3.6.57 1 1 0 0 1 1 1V20a1 1 0 0 1-1 1A17 17 0 0 1 3 4a1 1 0 0 1 1-1h3.5a1 1 0 0 1 1 1c0 1.25.2 2.45.57 3.57a1 1 0 0 1-.25 1z" fill="#fff"/></svg>123-456-7890</span>
</div>
<nav class="nav">
  <a style="margin-right:49px">Home</a><a style="margin-right:49px">About</a><a style="margin-right:49px">Services</a><a>Contact Us</a>
</nav>
<h1 class="hero-title">We Are A Waste Tire Recycling Company,<br>Providing A Sustainable And Cost Effective Service</h1>
<a class="btn" style="left:540px;top:268px;width:120px;height:39px">Contact Us</a>

<!-- ABOUT -->
<div class="about-panel"></div>
<div class="photo" role="img" aria-label="Recycling arrows framing photos of tires and recycling workers around a green leaf" style="left:404px;top:619px;width:388px;height:367px;border-radius:40%;background:radial-gradient(circle at 50% 50%,#5bb86e 0%,#4a5a4c 45%,#ffffff 72%)"></div>

<h2 class="heading abs" style="left:220px;top:1012px;color:var(--white)"><span class="dot" style="background:var(--white)"></span>About GravaLoop</h2>
<div class="abs about-copy" style="left:220px;top:1068px;width:435px">
  <p class="copy">GravaLoop is forging the way towards a more sustainable future through scrap tire collection &amp; waste tire recycling You've got a business to run, and we've got you covered. Let us worry about your <b>scrap tire removal</b> so you don't have to.</p>
  <p class="copy" style="margin-top:4px">Through the use of innovative technologies, we are not only more eco-friendly but able to pass the savings along to our customers.</p>
  <p class="copy" style="margin-top:4px">Waste Tire Management is a global problem that GravaLoop aims to resolve. Though our innovative approach to <b>waste tire management</b>, we are focused on resolving environmental concerns head-on. All while giving businesses across the region an opportunity to make a difference for the environment and their bottom line.</p>
</div>
<div class="photo" role="img" aria-label="Close-up of stacked black tires" style="left:690px;top:1020px;width:290px;height:363px;background:linear-gradient(160deg,#5a5d61,#1d1f22)"></div>
<div class="photo" role="img" aria-label="Worker in red jacket handling tires on warehouse shelving" style="left:220px;top:1418px;width:289px;height:420px;background:linear-gradient(180deg,#d9dadc,#8d9096 60%,#3a3c40)"></div>
<div class="abs about-copy" style="left:553px;top:1414px;width:445px">
  <p class="copy">Built upon a foundation of innovation, attention to detail, and budget-conscious services, GravaLoop is at the forefront of pushing the boundaries of what can be achieved through advancing technology. Through our rigorous procedures, environmental commitment we go beyond expectations. GravaLoop aims to achieve efficiency all while revolutionizing the industry.</p>
  <p class="copy" style="margin-top:4px">When your company is deciding on <b>used-tire disposal</b> responsibilities you can rest assured that GravaLoop has your company's interest at its core. Leave the costly equipment, manpower, and output-reducing duties to us. GravaLoop will help you focus your time where it counts.</p>
  <p class="copy" style="margin-top:4px">At our heart GravaLoop's focus is to always better our processes, support our industry, and environment. Here at GravaLoop we see ourselves as an extension of your team, outdoing competitors on speed, value, and price point.</p>
  <p class="copy" style="margin-top:4px;font-weight:700">Here at GravaLoop we're making a stand. Are you joining us</p>
</div>

<!-- SERVICES -->
<h2 class="heading abs" style="left:0;width:1200px;justify-content:center;top:1964px"><span class="dot"></span>Our <span class="accent">Services</span></h2>
<div class="abs" style="left:0;top:2067px;width:1200px;height:307px;background:var(--grey-band)"></div>
<div class="service-card" style="left:162px"><div class="photo" role="img" aria-label="Heap of discarded tires in a yard" style="background:linear-gradient(150deg,#8a7a68,#2b2b2b)"></div><h3>Waste Tire<br>Management &amp;<br>Recycling</h3></div>
<div class="service-card active" style="left:385px"><div class="photo" role="img" aria-label="Gloved hand inspecting a tire tread" style="background:linear-gradient(150deg,#4f5459,#1f2124 60%,#2f6db0)"></div><h3>Tire Remediation<br>&amp; Special Tire<br>Clean-Ups</h3></div>
<div class="service-card" style="left:610px"><div class="photo" role="img" aria-label="Laptop showing a scheduling calendar on a desk" style="background:linear-gradient(150deg,#f4f4f4,#b9bcc0)"></div><h3>Scheduling &amp;<br>Billing</h3></div>
<div class="service-card" style="left:833px"><div class="photo" role="img" aria-label="Support agent on a phone call taking notes" style="background:linear-gradient(150deg,#d8cfc6,#8a7b70)"></div><h3>First Rate<br>Customer Support<br>&amp; Service</h3></div>

<!-- REVIEWS -->
<h2 class="heading abs" style="left:0;width:1200px;justify-content:center;top:2441px"><span class="dot"></span>Clients <span class="accent">Review</span></h2>
<div class="abs" style="left:251px;top:2532px;width:220px;height:220px;background:#3b3b3b"></div>
<div class="photo" role="img" aria-label="Portrait of a smiling client" style="left:269px;top:2550px;width:184px;height:184px;background:linear-gradient(180deg,#e9e9e9,#c4b3a4)"></div>
<svg class="abs" style="left:262px;top:2510px" width="60" height="40" viewBox="0 0 60 40" aria-hidden="true">
  <path d="M4 40V22L14 0h10L16 20h10v20z" fill="var(--green)"/><path d="M32 40V22L42 0h10L44 20h10v20z" fill="var(--green)"/>
</svg>
<p class="copy abs" style="left:513px;top:2530px;width:450px">Lorem ipsum dolor sit amet, consectetuer adipiscing elit, sed diam nonummy nibh euismod tincidunt ut laoreet dolore magna aliquam erat volutpat. Ut wisi enim ad minim veniam, quis nostrud exerci tation ullamcorper suscipit lobortis nisl ut aliquip ex ea commodo consequat.</p>
<div class="abs" style="left:513px;top:2670px;font-size:14px;color:var(--ink)"><b style="font-weight:600">Marcus Dell</b>&nbsp;&nbsp;<span style="font-size:13px">Lorem ipsum dolor</span></div>
<svg class="abs" style="left:512px;top:2728px" width="80" height="20" viewBox="0 0 80 20" aria-hidden="true">
  <path d="M28 10H2M10 2L2 10l8 8" fill="none" stroke="#9a9a9a" stroke-width="1.6"/>
  <path d="M48 10h28M68 2l8 8-8 8" fill="none" stroke="var(--green)" stroke-width="1.6"/>
</svg>

<!-- PRODUCT -->
<svg class="abs" style="left:0;top:2825px" width="1200" height="560" viewBox="0 0 1200 560" aria-hidden="true">
  <polygon points="682,0 1200,0 1200,540 845,485" fill="var(--charcoal)"/>
  <polygon points="840,430 1200,430 1200,545 845,485" fill="var(--charcoal)"/>
  <polygon points="840,430 880,430 900,490 1200,545 845,485" fill="var(--green)"/>
</svg>
<h2 class="heading abs" style="left:162px;top:2906px"><span class="dot"></span>Our <span class="accent">Product</span></h2>
<p class="copy abs" style="left:162px;top:2966px;width:436px">TDF: GravaLoop seeks to be one of the leading TDF suppliers to the region. This is a product with a wide range of demand from pulp and paper mills, electrical utilities, industrial boilers to cement and asphalt plants our expertly handled tire-derived fuel is being used and receiving high marks for its ever-expanding list of benefits. From driving boiler efficiency to stamping out emissions, GravaLoop wants to be your TDF supplier offering additional services to include tire pick-up to TDF drop-off we have your back!</p>
<a class="btn" style="left:162px;top:3213px;width:120px;height:38px">Contact Us</a>
<div class="photo" role="img" aria-label="Pile of shredded tire chips used as tire-derived fuel" style="left:652px;top:2914px;width:386px;height:340px;background:linear-gradient(160deg,#5d6b52,#2a2a2a 55%,#4a4640)"></div>

<!-- COMMITMENT -->
<div class="photo" role="img" aria-label="Lone tree reflected in water under a dusk sky" style="left:0;top:3402px;width:754px;height:366px;background:linear-gradient(180deg,#1f2d44 0%,#334664 50%,#6c5440 80%,#2a2722 100%);clip-path:polygon(0 0,754px 0,550px 366px,0 366px)"></div>
<div class="photo" role="img" aria-label="Faint stacked tires in the background" style="left:820px;top:3420px;width:380px;height:360px;background:radial-gradient(ellipse at 60% 50%,#e4e4e4,#ffffff 70%)"></div>
<div class="abs" style="left:162px;top:3488px;color:#fff;font-family:'Roboto Condensed',sans-serif;font-weight:700">
  <div style="font-size:34px;line-height:44px">GravaLoop Is Committed To</div>
  <div style="font-size:24px;line-height:38px;margin-top:6px">Sustainability And Looking At Your Wast<br>Tires As A Means To Offer Innovation</div>
</div>
<a class="btn" style="left:162px;top:3633px;width:120px;height:38px">Contact Us</a>
<div class="abs" style="left:752px;top:3466px;font-family:'Roboto Condensed',sans-serif;font-weight:700;color:var(--green);font-size:54px;line-height:60px">300,000,000</div>
<div class="abs" style="left:752px;top:3532px;font-family:'Roboto Condensed',sans-serif;font-weight:700;color:#3a3a3a;font-size:27px;line-height:36px">Scrap Tires Are<br>Generated Annually<br>By GravaLoop</div>
<a class="btn" style="left:752px;top:3658px;width:120px;height:39px">Contact Us</a>

<!-- FOOTER -->
<div class="logo" style="left:0;width:1200px;justify-content:center;top:3856px;color:var(--ink)"><span class="mark" style="background:var(--green)"></span>GravaLoop</div>
<div class="footer-nav" style="left:396px">Home</div>
<div class="footer-nav" style="left:498px">About</div>
<div class="footer-nav" style="left:602px">Services</div>
<div class="footer-nav" style="left:723px">Contact Us</div>

<div class="contact-box" style="left:162px">
  <svg width="42" height="42" viewBox="0 0 42 42" aria-hidden="true"><circle cx="21" cy="24" r="16" fill="none" stroke="var(--green)" stroke-width="1.6"/><path d="M21 4a7 7 0 0 1 7 7c0 6-7 13-7 13s-7-7-7-13a7 7 0 0 1 7-7z" fill="#fff" stroke="var(--green)" stroke-width="1.6"/><circle cx="21" cy="11" r="2.5" fill="var(--green)"/></svg>
  <div>123, Building Name, Street<br>City, State XY 123456</div>
</div>
<div class="contact-box" style="left:466px;padding-left:62px">
  <svg width="38" height="38" viewBox="0 0 24 24" aria-hidden="true"><path d="M6.6 10.8a15.1 15.1 0 0 0 6.6 6.6l2.2-2.2a1 1 0 0 1 1-.25 11.4 11.4 0 0 0 3.6.57 1 1 0 0 1 1 1V20a1 1 0 0 1-1 1A17 17 0 0 1 3 4a1 1 0 0 1 1-1h3.5a1 1 0 0 1 1 1c0 1.25.2 2.45.57 3.57a1 1 0 0 1-.25 1z" fill="none" stroke="var(--green)" stroke-width="1.2"/><path d="M15 3a6 6 0 0 1 6 6M15 6a3 3 0 0 1 3 3" fill="none" stroke="var(--green)" stroke-width="1.2"/></svg>
  <div><b>Phone</b><br>123-456-7890</div>
</div>
<div class="contact-box" style="left:771px;padding-left:24px;gap:14px">
  <svg width="40" height="40" viewBox="0 0 40 40" aria-hidden="true"><rect x="4" y="14" width="32" height="22" fill="none" stroke="var(--green)" stroke-width="1.6"/><path d="M4 14l16 12 16-12" fill="none" stroke="var(--green)" stroke-width="1.6"/><rect x="10" y="4" width="20" height="16" fill="#fff" stroke="var(--green)" stroke-width="1.6"/><path d="M14 9h12M14 13h12" stroke="var(--green)" stroke-width="1.4"/></svg>
  <div style="font-size:12.5px"><b>Email</b><br>info@gravaloop.example</div>
</div>

<div class="abs" style="left:0;top:4123px;width:1200px;height:41px;background:var(--green);color:#fff;font-size:12.5px;display:flex;align-items:center;padding-left:162px">
  © 2022 GravaLoop. All Rights Reserved.
  <span style="position:absolute;left:888px;top:13px;width:15px;height:15px;border-radius:50%;background:#fff"></span>
  <span style="position:absolute;left:940px;top:13px;width:15px;height:15px;border-radius:50%;background:#fff"></span>
  <span style="position:absolute;left:992px;top:13px;width:15px;height:15px;border-radius:50%;background:#fff"></span>
</div>

</body>
</html>
```